FC Blavin - Creation of a AD banner for our yearly event

We are a local soccer club in Switzerland. We're organizing a event that will substitute to our yearly club dinner. We need a banner AD to promote on the social networks this event.
We would like to see design that use one or the 2 colors of the club (blue and red).
This Ad should link to a online shop where we can buy vouchers.

Requirements
Must have
• Logo of the club
Title : Souper de gala quand même
Call to action : Plus d'informations
Side texte : Grande Tombola
Banner size : W300xH250 or W300xH600
Nice to have
• Promotion texte: Soutenez le FC Blavin et les restaurateurs locaux

```html
<!DOCTYPE html>
<html lang="fr">
<head>
<meta charset="utf-8">
<title>FC Blavin – Souper de gala quand même</title>
<link href="https://fonts.googleapis.com/css2?family=Oswald:wght@500;600;700&display=swap" rel="stylesheet">
<style>
  :root {
    --club-red: #d0464c;
    --club-red-light: #e0787a;
    --club-red-deep: #b8343c;
    --club-blue: #2f6fc4;
    --club-navy: #1d2a44;
    --panel-blue: #cadcf3;
    --ink: #111111;
    --white: #ffffff;
  }
  * { margin: 0; padding: 0; box-sizing: border-box; }
  html, body {
    width: 1200px;
    height: 410px;
    overflow: hidden;
    background: var(--white);
  }
  .banner {
    position: relative;
    width: 1200px;
    height: 410px;
    overflow: hidden;
    font-family: "Oswald", "Arial Narrow", sans-serif;
  }
  .team-photo {
    position: absolute;
    left: 0;
    top: 0;
    width: 966px;
    height: 410px;
    background:
      linear-gradient(180deg, rgba(255,255,255,0.10) 0%, rgba(255,255,255,0) 45%),
      linear-gradient(90deg, var(--club-red-light) 0%, var(--club-red) 40%, var(--club-red) 70%, var(--club-red-deep) 100%);
  }
  .headline {
    position: absolute;
    left: 0;
    top: 0;
    width: 930px;
    height: 410px;
    color: var(--white);
    text-align: center;
  }
  .headline__title {
    position: absolute;
    left: 0;
    width: 100%;
    font-weight: 600;
    font-size: 106px;
    line-height: 1;
    letter-spacing: 0.5px;
  }
  .headline__title--first { top: 12px; }
  .headline__title--second { top: 110px; }
  .headline__raffle {
    position: absolute;
    left: 0;
    top: 212px;
    width: 100%;
    font-weight: 600;
    font-size: 58px;
    line-height: 1;
  }
  .headline__support {
    position: absolute;
    left: 0;
    top: 357px;
    width: 100%;
    font-weight: 500;
    font-size: 21px;
    line-height: 1;
    letter-spacing: 3.2px;
  }
  .club-panel {
    position: absolute;
    left: 966px;
    top: 0;
    width: 234px;
    height: 410px;
    background: var(--panel-blue);
  }
  .club-name {
    position: absolute;
    left: 0;
    top: 60px;
    width: 234px;
    display: flex;
    align-items: center;
    justify-content: center;
    gap: 12px;
    color: var(--club-navy);
    font-weight: 700;
    font-size: 42px;
    line-height: 1;
  }
  .club-name__dot {
    width: 26px;
    height: 26px;
    border-radius: 50%;
    background: var(--club-red);
    flex: none;
  }
  .cta {
    position: absolute;
    left: 976px;
    top: 357px;
    width: 214px;
    height: 40px;
    background: var(--ink);
    color: var(--white);
    display: flex;
    align-items: center;
    justify-content: center;
    font-weight: 500;
    font-size: 21px;
    text-decoration: none;
    letter-spacing: 0.2px;
  }
</style>
</head>
<body>
  <div class="banner">
    <div class="team-photo" role="img" aria-label="Photo d'équipe du FC Blavin en maillots rouges, teintée de rouge"></div>

    <div class="headline">
      <h1 class="headline__title headline__title--first">Souper de gala</h1>
      <p class="headline__title headline__title--second">quand même</p>
      <p class="headline__raffle">Grande Tombola</p>
      <p class="headline__support">Soutenez le FC Blavin et les restaurateurs locaux</p>
    </div>

    <aside class="club-panel">
      <div class="club-name">
        <span class="club-name__dot"></span>
        <span>FC Blavin</span>
      </div>
    </aside>

    <a class="cta" href="#">Plus d’informations</a>
  </div>
</body>
</html>
```